Cell phone repair

you can please design me business card

size 3.5" x 2"

colors blue and red

fixit dash logo (you get from my website fixitdashhq.com )

"We Come To You!

It is very simple! You tell us what phone you have, And we come to fix it."

phone number: 412.586.3094

website: www.fixitdashhq.com

email: info@fixitdashhq.com

```html
<!DOCTYPE html>
<html lang="en">
<head>
<meta charset="utf-8">
<title>fixit dash — business card</title>
<link rel="stylesheet" href="https://fonts.googleapis.com/css2?family=Work+Sans:wght@400;500;600&display=swap">
<style>
  :root {
    --backdrop: #1c1c1e;
    --card: #202022;
    --card-edge: #2a2a2d;
    --mark: #8e8e93;
    --mark-shape: #c9c9cc;
    --text: #f2f2f2;
    --blue: #1e9be0;
    --red: #e8262c;
  }
  * { margin: 0; padding: 0; box-sizing: border-box; }
  html, body {
    width: 1200px; height: 900px; overflow: hidden;
    background: var(--backdrop);
    font-family: "Work Sans", Arial, sans-serif;
    color: var(--text);
  }
  .canvas { position: relative; width: 1200px; height: 900px; }
  .card {
    position: absolute;
    width: 630px; height: 360px;
    background: linear-gradient(135deg, var(--card-edge) 0%, var(--card) 60%);
    box-shadow: 0 18px 40px rgba(0,0,0,.55);
  }
  .card--front { left: 380px; top: 60px; }
  .card--back  { left: 190px; top: 480px; }

  .brand {
    position: absolute;
    display: flex; align-items: center; gap: 18px;
  }
  .brand__name {
    font-weight: 500;
    color: var(--mark);
    letter-spacing: .5px;
  }
  .brand__square {
    background: var(--mark-shape);
    border-radius: 8px;
  }
  .card--front .brand { left: 165px; top: 135px; }
  .card--front .brand__name { font-size: 46px; }
  .card--front .brand__square { width: 76px; height: 96px; }

  .card--back .brand { left: 40px; top: 140px; }
  .card--back .brand__name { font-size: 36px; }
  .card--back .brand__square { width: 58px; height: 76px; }

  .divider {
    position: absolute; left: 338px; top: 62px;
    width: 3px; height: 236px; background: var(--blue);
  }
  .details { position: absolute; left: 366px; top: 62px; }
  .details__name {
    font-size: 31px; font-weight: 500; line-height: 1; letter-spacing: .5px;
  }
  .details__first { color: var(--blue); }
  .details__last { color: var(--red); }
  .details__role { font-size: 17px; margin-top: 4px; }
  .details__address { font-size: 17px; line-height: 1.3; margin-top: 20px; letter-spacing: .5px; }
  .contact { list-style: none; margin-top: 14px; font-size: 17px; line-height: 1.45; letter-spacing: .5px; }
  .contact__item { display: flex; align-items: center; gap: 10px; }
  .contact__icon { width: 12px; height: 12px; flex: none; }
  .contact__accent { color: var(--blue); }
</style>
</head>
<body>
<div class="canvas">
  <section class="card card--front" aria-label="Card front">
    <div class="brand">
      <span class="brand__name">fixit dash</span>
      <span class="brand__square"></span>
    </div>
  </section>

  <section class="card card--back" aria-label="Card back">
    <div class="brand">
      <span class="brand__name">fixit dash</span>
      <span class="brand__square"></span>
    </div>
    <div class="divider"></div>
    <div class="details">
      <h1 class="details__name"><span class="details__first">DANIEL</span> <span class="details__last">REEVES</span></h1>
      <p class="details__role">Director</p>
      <p class="details__address">1847 Harlow Street<br>Brookfield, KY 40511</p>
      <ul class="contact">
        <li class="contact__item">
          <svg class="contact__icon" viewBox="0 0 12 12"><path d="M2.5 1 L4.5 1 L5 3.5 L3.8 4.5 Q5 7 7.5 8.2 L8.5 7 L11 7.5 L11 9.5 Q10 11 8.5 11 Q1 9 1 2.5 Q1 1.5 2.5 1 Z" fill="var(--blue)"/></svg>
          <span>412.586.3094</span>
        </li>
        <li class="contact__item">
          <svg class="contact__icon" viewBox="0 0 12 12"><rect x="1" y="2.5" width="10" height="7" fill="none" stroke="var(--blue)" stroke-width="1.2"/><path d="M1 2.5 L6 6.5 L11 2.5" fill="none" stroke="var(--blue)" stroke-width="1.2"/></svg>
          <span>info@fixitdashhq.com</span>
        </li>
        <li class="contact__item">
          <svg class="contact__icon" viewBox="0 0 12 12"><circle cx="6" cy="6" r="5" fill="none" stroke="var(--blue)" stroke-width="1.1"/><ellipse cx="6" cy="6" rx="2.2" ry="5" fill="none" stroke="var(--blue)" stroke-width="1"/><path d="M1 6 H11" stroke="var(--blue)" stroke-width="1"/></svg>
          <span>www.<span class="contact__accent">fixitdashhq</span>.com</span>
        </li>
      </ul>
    </div>
  </section>
</div>
</body>
</html>
```